business card with logo

Would like a business card for an electrical contractor called BRANLOCK ELECTRICS.
No generic electrical imagery (light globe, powerpoints, ect). Would like a logo or symbol created in the design as part of the project . I would like crisp colour. No templated designs like Printvox

is there any other designers willing to submit designs

Electrical

```html
<!DOCTYPE html>
<html lang="en">
<head>
<meta charset="utf-8">
<title>Branlock Electrics – Business Card</title>
<link href="https://fonts.googleapis.com/css2?family=Exo+2:wght@400;500;700&display=swap" rel="stylesheet">
<style>
  :root {
    --backdrop: #8f9193;
    --card-white: #ffffff;
    --card-grey-light: #f4f4f4;
    --card-grey-mid: #e2e2e2;
    --brand-blue: #12a8e6;
    --block-grey: #6a6a6a;
    --ink-dark: #3a3a3a;
    --ink-soft: #555555;
  }
  * { box-sizing: border-box; margin: 0; padding: 0; }
  html, body { width: 1200px; height: 894px; overflow: hidden; }
  body {
    background: var(--backdrop);
    font-family: "Exo 2", sans-serif;
    position: relative;
  }
  .card {
    position: absolute;
    left: 270px;
    width: 660px;
    height: 377px;
    overflow: hidden;
    box-shadow: 0 6px 18px rgba(0,0,0,0.25);
  }
  .card-front { top: 40px; background: var(--card-white); }
  .card-back {
    top: 477px;
    background: linear-gradient(120deg, var(--card-grey-light) 0%, var(--card-white) 45%, var(--card-grey-mid) 100%);
  }

  .front-name {
    position: absolute;
    left: 0; right: 0; top: 170px;
    display: flex; align-items: center; justify-content: center;
    gap: 14px;
    color: var(--brand-blue);
    font-weight: 500;
    font-size: 30px;
    line-height: 1;
    letter-spacing: 3px;
  }
  .front-mark {
    width: 22px; height: 22px;
    background: var(--brand-blue);
    flex: none;
  }

  .back-name {
    position: absolute;
    left: 40px; top: 52px;
    color: var(--brand-blue);
    font-weight: 700;
    font-size: 25px;
    letter-spacing: 0.5px;
  }
  .grey-block {
    position: absolute;
    left: 70px; top: 98px;
    width: 132px; height: 46px;
    background: var(--block-grey);
  }
  .blue-band {
    position: absolute;
    left: 202px; top: 144px;
    right: 0; height: 44px;
    background: var(--brand-blue);
    color: var(--card-white);
    font-size: 17px;
    letter-spacing: 1px;
    display: flex; align-items: center;
    padding-left: 95px;
  }
  .person {
    position: absolute;
    right: 40px; top: 92px;
    color: var(--ink-dark);
  }
  .person-name { font-size: 21px; font-weight: 500; letter-spacing: 1.5px; }
  .person-role { font-size: 12px; letter-spacing: 2px; }

  .contact-list, .web-list {
    position: absolute;
    list-style: none;
    font-size: 12px;
    color: var(--ink-soft);
    letter-spacing: 0.5px;
  }
  .contact-list { left: 28px; top: 156px; }
  .web-list { left: 330px; top: 262px; }
  .contact-list li, .web-list li {
    display: flex; align-items: center; gap: 10px;
    height: 24px;
  }
  .icon-tile {
    width: 16px; height: 16px;
    background: var(--brand-blue);
    display: flex; align-items: center; justify-content: center;
    flex: none;
  }
  .icon-tile svg { width: 10px; height: 10px; }
</style>
</head>
<body>

  <section class="card card-front" aria-label="Business card front">
    <div class="front-name"><span class="front-mark"></span>BRANLOCK ELECTRICS</div>
  </section>

  <section class="card card-back" aria-label="Business card back">
    <div class="back-name">BRANLOCK ELECTRICS</div>
    <div class="grey-block"></div>
    <div class="blue-band">www.branlockelectrics.com/au</div>

    <div class="person">
      <div class="person-name">ALAN REYES</div>
      <div class="person-role">MANAGER</div>
    </div>

    <ul class="contact-list">
      <li>
        <span class="icon-tile"><svg viewBox="0 0 10 10"><path d="M5 0.5a3 3 0 0 1 3 3c0 2.3-3 6-3 6s-3-3.7-3-6a3 3 0 0 1 3-3z" fill="#fff"/><circle cx="5" cy="3.5" r="1" fill="#12a8e6"/></svg></span>
        14 Harlow Street 4102
      </li>
      <li>
        <span class="icon-tile"><svg viewBox="0 0 10 10"><path d="M2 1h2l1 2.5-1.2 1a6 6 0 0 0 2.7 2.7l1-1.2L10 7v2a1 1 0 0 1-1 1C4.6 10 0 5.4 0 1a1 1 0 0 1 1-1z" fill="#fff"/></svg></span>
        012 480 3157
      </li>
      <li>
        <span class="icon-tile"><svg viewBox="0 0 10 10"><rect x="0.5" y="2" width="9" height="6" fill="none" stroke="#fff"/><path d="M0.5 2L5 5.5 9.5 2" fill="none" stroke="#fff"/></svg></span>
        office@branlock.com
      </li>
    </ul>

    <ul class="web-list">
      <li>
        <span class="icon-tile"><svg viewBox="0 0 10 10"><circle cx="5" cy="5" r="4" fill="none" stroke="#fff"/><path d="M1 5h8M5 1c-2 2.5-2 5.5 0 8M5 1c2 2.5 2 5.5 0 8" fill="none" stroke="#fff" stroke-width="0.8"/></svg></span>
        www.branlockelectrics.com
      </li>
      <li>
        <span class="icon-tile"><svg viewBox="0 0 10 10"><circle cx="5" cy="5" r="3" fill="#fff"/></svg></span>
        www.branlock.social
      </li>
      <li>
        <span class="icon-tile"><svg viewBox="0 0 10 10"><circle cx="5" cy="5" r="3" fill="#fff"/></svg></span>
        www.branlock.community
      </li>
    </ul>
  </section>

</body>
</html>
```